Brochure Design Project

UCWA
The brochure is intended to be on United Council of Wellness Arts website available for the members to download for the purpose of educating public about benefits of clinical hypnosis and introduce it as possible treatment option. There should be a empty space left on the last page for the member to stamp their office information.
So, the intended audience is general public that might be interested in hypnosis treatment
White on blue is logo of UCWA.
I would like the brochure to have bright complimentary colors with imagery that is used in health care/complimentary medicine - nature, relaxation, etc.
UCWA website is UCWAinfo.net.

```html
<!DOCTYPE html>
<html lang="en">
<head>
<meta charset="UTF-8">
<title>Clinical Hypnosis – Inside Panels</title>
<link rel="stylesheet" href="https://fonts.googleapis.com/css2?family=Arimo:ital,wght@0,400;0,700;1,700&display=swap">
<style>
  :root{
    --navy:#23275a;
    --ink:#2b2b2b;
    --paper:#ffffff;
    --bg-soft:#eef0f3;
  }
  *{margin:0;padding:0;box-sizing:border-box}
  html,body{width:1200px;height:927px;overflow:hidden}
  body{font-family:"Arimo",Arial,sans-serif;color:var(--ink);background:var(--paper)}
  .sheet{position:relative;width:1200px;height:927px;overflow:hidden}
  .backdrop{position:absolute;inset:0;background:linear-gradient(135deg,#ffffff 0%,var(--bg-soft) 45%,#ffffff 70%,#e9ebef 100%)}
  .column{position:absolute;top:0;height:927px}
  .col-left{left:12px;width:364px}
  .col-mid{left:402px;width:372px}
  .col-right{left:818px;width:370px}
  .block{position:absolute;left:0;right:0}
  .section-head{position:relative;height:22px;margin-bottom:24px}
  .section-head::after{content:"";position:absolute;left:0;right:0;top:10px;height:2px;background:var(--navy)}
  .section-head span{position:relative;z-index:1;display:inline-block;height:22px;line-height:22px;padding:0 22px 0 10px;
    background:var(--navy);color:#fff;font-weight:700;font-style:italic;font-size:16px;border-radius:0 11px 11px 0}
  p,li{font-size:14px;line-height:19.3px;text-align:justify}
  .bullets{list-style:none}
  .bullets li{position:relative;padding-left:21px;margin-bottom:0}
  .bullets li::before{content:"";position:absolute;left:1px;top:6px;width:7px;height:7px;background:var(--navy)}
  .bullets.spaced li{margin-bottom:1px}
  .lead{font-weight:700;font-style:italic;color:var(--navy)}
  .tight li{text-align:left}
</style>
</head>
<body>
<div class="sheet">
  <div class="backdrop" role="img" aria-label="Soft light grey geometric cube pattern background"></div>

  <section class="column col-left">
    <div class="block" style="top:33px">
      <h2 class="section-head"><span>What it is</span></h2>
      <ul class="bullets">
        <li>Hypnosis is considered to be a state of focused attention and inner absorption; there is decreased awareness of surroundings and increased ability to respond to acceptable suggestions.</li>
        <li>A collaborative process that helps a person's mind and body function more comfortably and effectively.</li>
        <li>It is not uncommon for all of us to experience a situation when we are so preoccupied with a thought or experience that we neglect surroundings. Examples – watching a favorite show, computer games or driving under "highway" hypnosis.</li>
        <li>It requires special training to use hypnosis appropriately in medicine, dentistry and psychotherapy and should be done by licensed professionals in respected fields.</li>
      </ul>
    </div>
    <div class="block" style="top:493px">
      <h2 class="section-head"><span>What it is not</span></h2>
      <p>It is not a mind control, just a suggestion.<br>
      It cannot be imposed on an unwilling or uninterested person<br>
      It is not a miracle or cure, but a way to solve some problems.</p>
    </div>
    <div class="block" style="top:689px">
      <h2 class="section-head"><span>Why use hypnosis</span></h2>
      <ul class="bullets">
        <li>Hypnosis is unique in its ability to help you unlock imagination, bypass the "can never happen" censor of the conscious mind, and simply help one see experiences and memories in a different light.</li>
        <li>It can help find solutions and resolutions to a difficult mental or physical problem, and find inner sources of strength and resilience.</li>
      </ul>
    </div>
  </section>

  <section class="column col-mid">
    <div class="block" style="top:12px">
      <ul class="bullets">
        <li>It can help a person better understand one's own as well as others' motivations and behavior.</li>
        <li>It allows a person to choose and develop abilities and capacities that can help achieve a desired goal.</li>
        <li>During the process of hypnosis a person is frequently taught how use individualized cues and techniques to achieve desired result (decrease anxiety, reduce pain, improve sport performance, etc.) With practice, a person can achieve a level of control that seemed impossible before.</li>
      </ul>
    </div>
    <div class="block" style="top:274px">
      <h2 class="section-head"><span>When</span></h2>
      <p style="text-align:left">Hypnosis has been found to be very effective for treating many mental and physical conditions, as well improving physical and mental performance, and changing undesirable habits.</p>
      <p class="lead">Its applications can include:</p>
      <ul class="bullets spaced tight">
        <li>anxiety disorders;</li>
        <li>coping with emotional and physical trauma;</li>
        <li>insomnia;</li>
        <li>acute and chronic pain relief;</li>
        <li>preparation for surgical procedures;</li>
        <li>childbirth;</li>
        <li>decreasing side effects of chemotherapy and radiation;</li>
        <li>gastrointestinal disorders;</li>
        <li>asthma;</li>
        <li>sports performance and tests preparation;</li>
        <li>fear of flying and</li>
        <li>smoking cessation and weight control</li>
      </ul>
    </div>
    <div class="block" style="top:783px">
      <h2 class="section-head"><span>How</span></h2>
      <p>A person conducting hypnosis will walk you through the process, help define goals and expectations, and explain how you can achieve the results you want.</p>
    </div>
  </section>

  <section class="column col-right">
    <div class="block" style="top:4px">
      <p>Hypnosis starts with an induction process : you simply concentrate on an object, idea or symbol. Induction is followed by relevant communication and crafting of the suggestion. The last step is reorientation and discussion of the experience, and instruction on home practice. All hypnosis is ultimately a form of self hypnosis.</p>
    </div>
    <div class="block" style="top:203px">
      <h2 class="section-head"><span>Is Hypnosis right for me?</span></h2>
      <p>Hypnosis is a wonderful and effective tool. If you are not familiar with hypnosis, you might worry about loss of control and embarrassment. People are also worried that their problems cannot be helped.<br>
      Hypnosis might offer a novel way to approach or resolve the problem, or just see it in a different light. Even if hypnosis does not immediately solve the problem, you can still learn how to be a little more comfortable and experience a deeper level of physical and mental relaxation.</p>
    </div>
    <div class="block" style="top:518px">
      <h2 class="section-head"><span>Practice will help.</span></h2>
      <p>Well-trained medical or mental health professionals will help you discover and use resources and strengths that you did not know you had.<br>
      Your therapist, doctor or dentist might be the best person to discuss hypnosis and how it can be helpful to you.<br>
      Licensed professionals get their training and certification through the United Council of Wellness Arts. You can find a list of certified providers on UCWAinfo.net.</p>
    </div>
  </section>
</div>
</body>
</html>
```